Technical Communications firm needs an article turned into a white paper

We want to redesign a 3-part blog series into a white paper that we can print for a conference. I've consolidated the three posts into the attached Word document.

We are looking for a light, easy to read design. Good use of graphics to support the message. I've added the graphics we used in the original post.

You can view them at
http://www.lanternquill.com/blog/are-you-satisfied-with-your-dita-solution/

Target Market(s)

Product managers from High-tech, Finance, and Medical industries.

Industry/Entity Type

Information Technology

Colors

Designer to choose colors to be used in the design.

Requirements
Must have
• Must be modern, light, easy to read and slick design. Try to incorporate the graphics provided, but feel free to add more. Must retain the lists and tables.
• Must align with our website/brand.
• Must be easy to read. So not too busy.
• Please move all footnotes to endnotes. You'll need to rework the numbering.
Nice to have
• Awesome coverpage.
Should not have
• Hokey clipart. Not too heavy or hard to read.

```html
<!DOCTYPE html>
<html lang="en">
<head>
<meta charset="utf-8">
<title>White Paper Spreads – Lantern Quill</title>
<link rel="stylesheet" href="https://fonts.googleapis.com/css2?family=Open+Sans:wght@300;400;600;700&display=swap">
<style>
:root{
  --canvas:#ffffff;
  --paper:#ffffff;
  --ink:#2e2e2e;
  --brand-blue:#1f55b4;
  --brand-blue-dark:#1a47a0;
  --sky-blue:#3c86cf;
  --teal:#3fa7b2;
  --green:#6cc4a4;
  --heading:#3a72c4;
  --label:#d6e6f7;
}
*{box-sizing:border-box;margin:0;padding:0}
html,body{width:1200px;height:1200px;overflow:hidden;background:var(--canvas)}
body{position:relative;font-family:"Open Sans",Arial,sans-serif;color:var(--ink)}
.page{position:absolute;background:var(--paper);box-shadow:0 2px 7px rgba(0,0,0,.38);overflow:hidden}
.p1{left:116px;top:42px;width:302px;height:390px}
.p2{left:459px;top:42px;width:302px;height:390px}
.p3{left:800px;top:42px;width:300px;height:390px}
.p4{left:116px;top:448px;width:298px;height:384px}
.p5{left:459px;top:448px;width:294px;height:384px}
.p6{left:803px;top:448px;width:294px;height:384px}
.p7{left:298px;top:804px;width:294px;height:380px}
.p8{left:636px;top:804px;width:294px;height:380px}

.masthead{position:absolute;left:0;top:0;width:100%;height:64px}
.masthead svg{display:block;width:100%;height:100%}
.brand{position:absolute;left:42px;top:36px;display:flex;align-items:center;gap:3px;color:#fff;font-size:6px;font-weight:600;line-height:1}
.brand .dot{width:9px;height:9px;border-radius:50%;background:#fff}
.section-label{position:absolute;right:28px;top:27px;font-size:3.8px;line-height:4px;letter-spacing:.5px;color:var(--label);text-transform:uppercase}

.column{position:absolute;left:98px;top:104px;width:182px;font-size:3.9px;line-height:5.5px;text-align:justify}
.column h2{font-weight:300;font-size:8.4px;line-height:9px;color:var(--heading);margin:10px 0 2px;text-align:left}
.column h2:first-child{margin-top:0}
.column ul{list-style:none;margin:5px 0 5px 18px;text-align:left}
.column li{position:relative;padding-left:4px}
.column li::before{content:"•";position:absolute;left:0}
.endnotes{position:absolute;left:42px;width:190px;font-size:2.8px;line-height:3.7px;border-top:.5px solid #bbb;padding-top:3px}

.cover-photo{position:absolute;left:0;top:0;width:100%;height:152px;background:linear-gradient(180deg,#c9d8e8 0%,#e6edf3 55%,#d9e2ea 100%)}
.part-band{position:absolute;left:20px;right:0;top:106px;height:16px;background:var(--sky-blue);color:#dce9f8;font-size:7px;line-height:16px;padding-left:10px}
.title-band{position:absolute;left:20px;right:0;top:124px;height:34px;background:linear-gradient(90deg,#2b74b9,#3f9fb6 70%,#58b6b0);color:#fff;font-size:15px;font-weight:300;line-height:34px;padding-left:22px;letter-spacing:.3px}
.cover-text{position:absolute;left:96px;top:172px;width:182px;font-size:3.9px;line-height:5.5px;text-align:justify}
.dropcap{float:left;font-size:30px;line-height:24px;color:var(--brand-blue-dark);margin:0 3px 0 0}
.cover-text h2{font-weight:300;font-size:8.4px;line-height:9px;color:var(--heading);margin:14px 0 2px;text-align:left}
.cover-text ul{list-style:none;margin:5px 0 5px 18px;text-align:left}
.cover-text li{position:relative;padding-left:4px}
.cover-text li::before{content:"•";position:absolute;left:0}

.back-band{position:absolute;left:82px;top:0;width:130px;height:32px;background:linear-gradient(180deg,#1f55b4 0 60%,#3f8fc4 60%,#5ab8b0 100%)}
.back-col{position:absolute;left:80px;top:76px;width:135px;font-size:3.9px;line-height:5.5px;text-align:justify}
.back-col h3{font-weight:300;font-size:6.6px;line-height:7px;color:var(--heading);text-align:center;margin-bottom:5px}
.back-col .spacer{height:26px}
.back-brand{position:absolute;left:96px;top:322px;display:flex;align-items:center;gap:4px;font-size:9px;font-weight:600;color:var(--brand-blue)}
.back-brand .dot{width:14px;height:14px;border-radius:50%;background:var(--brand-blue)}
</style>
</head>
<body>

<section class="page p1">
  <div class="masthead">
    <svg viewBox="0 0 300 64" preserveAspectRatio="none">
      <defs><linearGradient id="stripe1" x1="0" x2="1"><stop offset="0" stop-color="#3c8fd0"/><stop offset=".45" stop-color="#4aa9c0"/><stop offset="1" stop-color="#5fc0a8"/></linearGradient></defs>
      <rect width="300" height="24" fill="#1f55b4"/>
      <polygon points="0,24 300,24 300,50 238,50 226,62 0,62" fill="url(#stripe1)"/>
      <polygon points="0,46 300,38 300,46 0,52" fill="#2e6fc3" opacity=".55"/>
      <line x1="0" y1="62" x2="226" y2="62" stroke="#7fd0b0" stroke-width="1"/>
    </svg>
    <div class="brand"><span class="dot"></span>LANTERN QUILL</div>
    <div class="section-label">Technology</div>
  </div>
  <div class="column" style="top:146px">
    <p>your existing system and put it into an entirely new system with relatively minor disruption. Or if your entire system isn't the problem, you can often replace components of your solution with components from other vendors to achieve a better result. Lastly, because your content is in XML, it can often be refactored to correct problems that have accumulated in your content over time.</p>
    <p>Before we look at changing your technology, we should examine some of these problems to see if we can identify a more appropriate root cause.</p>
    <h2>Performance problems</h2>
    <p>Common complaints regarding performance include observations that processes take longer or systems are slower to respond than they were before the move to DITA. Part of this observation may be related to aligning to different expectations. You are working with a lot more parts and potentially with many more people to get the job done. Some parts of the process will naturally take longer. These perceived issues will appear worse when you are required to collaborate with writers, editors, and other team members across great distances.</p>
    <p>If the overall time and effort does not significantly improve over the course of 2-3 production life cycles of the content, then there may be some other issues at play. You'll want to examine your</p>
    <ul>
      <li>Processes – Have you eliminated redundant activities in your processes?</li>
      <li>Pipes – Is your productivity impeded by network performance?</li>
      <li>Platforms – Are users experiencing problems related to disparate desktop configurations?</li>
      <li>Processors – Are your servers or client machines underpowered for the tools?</li>
      <li>People – Do your users follow established best practices for working with your tools?</li>
    </ul>
    <p>Once you've identified all external factors affecting performance, you'll want to examine how your tools are configured and deployed. There may be alternative features, configurations, or components that will greatly improve system performance. Your tool vendors or service providers should be able to help you examine your options.</p>
  </div>
</section>

<section class="page p2">
  <div class="masthead">
    <svg viewBox="0 0 300 64" preserveAspectRatio="none">
      <defs><linearGradient id="stripe2" x1="0" x2="1"><stop offset="0" stop-color="#3c8fd0"/><stop offset=".45" stop-color="#4aa9c0"/><stop offset="1" stop-color="#5fc0a8"/></linearGradient></defs>
      <rect width="300" height="24" fill="#1f55b4"/>
      <polygon points="0,24 300,24 300,50 238,50 226,62 0,62" fill="url(#stripe2)"/>
      <polygon points="0,46 300,38 300,46 0,52" fill="#2e6fc3" opacity=".55"/>
      <line x1="0" y1="62" x2="226" y2="62" stroke="#7fd0b0" stroke-width="1"/>
    </svg>
    <div class="brand"><span class="dot"></span>LANTERN QUILL</div>
    <div class="section-label">Technology</div>
  </div>
  <div class="column" style="top:120px">
    <h2>Complexity problems</h2>
    <p>Finding the correct balance of complexity versus utility is one of the biggest challenges we face in DITA deployments. The problem may not be that your tools are too complex, rather that too much complexity is exposed to the wrong group of users. The best-architected systems attempt to push the most complexity onto the shoulders of the fewest number of people. As much as possible, let the software handle most of the heavy lifting.</p>
    <p>It's important to note that collaborative, structured authoring is always going to be more complex than traditional desktop publishing. Despite attempts to simplify the technology around content authoring, content itself is not getting any simpler. Dale Pruitt of Cobalt Insight believes that content development practices and technology are following trends we see in other related industries. His predictions are that content development will continue to become much more</p>
    <ul>
      <li>precise</li>
      <li>complex</li>
      <li>collaborative, and</li>
      <li>integrated into larger enterprise systems.</li>
    </ul>
    <p style="margin-top:8px">To strike the proper balance between complexity and utility you need to consider how the technology decisions you make now impact the viability of your content in the future. Will simpler structures, semantics, and metadata cause significant rework in the future to attain your goals? Or, will postponing certain complexities increase the likelihood for adoption and pave the way for early wins? The only way to answer these questions is to map out your long-term goals and assess the steps you will take to get there.</p>
  </div>
</section>

<section class="page p3">
  <div class="masthead">
    <svg viewBox="0 0 300 64" preserveAspectRatio="none">
      <defs><linearGradient id="stripe3" x1="0" x2="1"><stop offset="0" stop-color="#3c8fd0"/><stop offset=".45" stop-color="#4aa9c0"/><stop offset="1" stop-color="#5fc0a8"/></linearGradient></defs>
      <rect width="300" height="24" fill="#1f55b4"/>
      <polygon points="0,24 300,24 300,50 238,50 226,62 0,62" fill="url(#stripe3)"/>
      <polygon points="0,46 300,38 300,46 0,52" fill="#2e6fc3" opacity=".55"/>
      <line x1="0" y1="62" x2="226" y2="62" stroke="#7fd0b0" stroke-width="1"/>
    </svg>
    <div class="brand"><span class="dot"></span>LANTERN QUILL</div>
    <div class="section-label">Technology</div>
  </div>
  <div class="column" style="top:122px">
    <h2>Steps to address complexity</h2>
    <p>The first step to understanding your needs is to assess your level of process maturity against industry benchmarks. There are a few models to choose from including the Structured Content Maturity Ladder. Once you've determined your current state, you can decide upon your timing to achieve your target state and map out the steps to get there.</p>
    <p>The second step is to develop a content strategy and roadmap that speak to your goals and capabilities you need to achieve over the next two years. Your strategy should align with your business goals and direction. Plan for a minor review every 6 months and a major review each year to determine your funding requirements to stay the course with your roadmap.</p>
    <p>By understanding your plan and getting sign-off from stakeholders, you will be able to determine whether you should</p>
    <ul style="margin-left:22px">
      <li>eliminate certain elements that are unnecessarily complex</li>
      <li>hire more staff to assume responsibility for some of the more complex tasks</li>
      <li>invest more time and money in training to compensate for complexity</li>
      <li>invest more money in tools that better mask the complexity, or</li>
      <li>re-engineer certain aspects of your processes.</li>
    </ul>
    <h2>Lantern Quill® Health Check</h2>
    <p>Before making any moves to replace your current technology stack, let us work with you to assess your needs and review the current state of your deployment. We may be able to discover areas for improvement and extend the usefulness of your existing technology. If you need new tools, we can help you with that as well. Sometimes we all just need to stop throwing more technology at our content problems. Learn more about our workshops.</p>
  </div>
  <div class="endnotes" style="top:324px;width:250px">
    <p>[i] The Structured Content Contentment Poll, published by The Copy Ranch in spring 2017. An analysis of the results by Reid Halvorsen and the poll team is in the TalkStage archive.</p>
    <p>[ii] Working Together on Shared Topics, a talk by Reid Halvorsen at the Topic Authoring Forum, 2017.</p>
    <p>[iii] The Structured Content Maturity Ladder, an open guide to staged adoption, 2008.</p>
  </div>
</section>

<section class="page p4">
  <div class="cover-photo" role="img" aria-label="Photograph of a cluster of yellow, green and red road signs with arrows against a pale cloudy sky"></div>
  <div class="part-band">PART 3</div>
  <div class="title-band">MANAGEMENT</div>
  <div class="cover-text">
    <p><span class="dropcap">T</span>his article is part of a series based on the results of a survey of more than 250 technical communication professionals conducted by The Copy Ranch in 2017 entitled The Structured Content Contentment Poll. In the survey, almost two-thirds of respondents voiced some concerns with their DITA deployment.</p>
    <p>In my previous article in the series, I examined some of the principle issues related to technology. This last article in the series looks at the role management can play in improving user satisfaction with DITA.</p>
    <h2>Issues related to management</h2>
    <p>The lowest ranked reported issues fall under the category of management. These include</p>
    <ul>
      <li>We are impeded by a lack of governance. Ranked 6th by 60% of respondents</li>
      <li>We cannot find the right people to fill key roles. Ranked 7th by 57% of respondents, and</li>
      <li>We are unable to measure success. Ranked 9th by 55% of respondents.</li>
    </ul>
    <p>While these issues appear to be of least concern to many respondents, they are most likely to form the root cause of all other issues identified in the survey. This points to a general lack of awareness as to the role management should be playing in collaborative, structured authoring solutions.</p>
    <p>Organizations that lag in management of their structured authoring solutions of-</p>
  </div>
</section>

<section class="page p5">
  <div class="masthead">
    <svg viewBox="0 0 300 64" preserveAspectRatio="none">
      <defs><linearGradient id="stripe5" x1="0" x2="1"><stop offset="0" stop-color="#3c8fd0"/><stop offset=".45" stop-color="#4aa9c0"/><stop offset="1" stop-color="#5fc0a8"/></linearGradient></defs>
      <rect width="300" height="24" fill="#1f55b4"/>
      <polygon points="0,24 300,24 300,50 238,50 226,62 0,62" fill="url(#stripe5)"/>
      <polygon points="0,46 300,38 300,46 0,52" fill="#2e6fc3" opacity=".55"/>
      <line x1="0" y1="62" x2="226" y2="62" stroke="#7fd0b0" stroke-width="1"/>
    </svg>
    <div class="brand"><span class="dot"></span>LANTERN QUILL</div>
    <div class="section-label">Management</div>
  </div>
  <div class="column" style="left:93px;top:90px;width:188px">
    <p>ten put technology ahead of process; or worse, they embark down the road of content management without any intention of actually managing content or the people who create it. "We cannot tell our writers how to write," is a common excuse for failing to manage content and govern content creation efforts.</p>
    <p>Organizations that see DITA as a magical fast-path to the bleeding edge of technology—or a panacea for multichannel publishing—are most likely to fail. Organizations that understand the importance of planning, experimentation and governance are more likely to experience success.</p>
    <h2>Planning strategies</h2>
    <p>Planning starts with a solid understanding of the issues your organization faces that point to structured authoring as a possible solution. This involves research to determine pain points and gather baseline metrics that will help you to measure success. This research forms the basis of your business case.</p>
    <p>Good planning means that you understand how this initiative will impact your current staff and possibly increase headcount to ensure you have the right people in the right roles. If you have absolutely no ability to affect headcount—or reassign staff—then you will find yourself seriously hampered in the early stages of your DITA deployment.</p>
    <p>Ten years ago, it wasn't uncommon to see attrition rates as high as 30% when technical publication groups transitioned to topic-based, structured authoring from more traditional desktop publishing. Today these numbers have come down as more technical writers adapt to their changing environment and demand for qualified DITA authors increases.</p>
    <p>Understand that planning is not something you do once and move on. Planning needs to be iterative allowing you to roll out a minimum viable solution as early as possible and then add on increased complexity and sophistication over time as needed. Your needs will change, sometimes quickly.</p>
    <h2>Experimentation strategies</h2>
    <p>The importance of planned experimentation and how it plays into the growth of your structured authoring solution cannot be understated. Your experimentation begins with your first proof-of-concept (PoC) to demonstrate the advantages of structured authoring and validate your business case. Here is it important to keep your costs low and workplace disruption to a minimum. The success of your PoC should validate the costs for proceeding to the pilot.</p>
  </div>
</section>

<section class="page p6">
  <div class="masthead">
    <svg viewBox="0 0 300 64" preserveAspectRatio="none">
      <defs><linearGradient id="stripe6" x1="0" x2="1"><stop offset="0" stop-color="#3c8fd0"/><stop offset=".45" stop-color="#4aa9c0"/><stop offset="1" stop-color="#5fc0a8"/></linearGradient></defs>
      <rect width="300" height="24" fill="#1f55b4"/>
      <polygon points="0,24 300,24 300,50 238,50 226,62 0,62" fill="url(#stripe6)"/>
      <polygon points="0,46 300,38 300,46 0,52" fill="#2e6fc3" opacity=".55"/>
      <line x1="0" y1="62" x2="226" y2="62" stroke="#7fd0b0" stroke-width="1"/>
    </svg>
    <div class="brand"><span class="dot"></span>LANTERN QUILL</div>
    <div class="section-label">Management</div>
  </div>
  <div class="column" style="left:90px;top:84px;width:188px">
    <p>Second phase of experimentation occurs with the design and execution of the pilot project. The pilot will rely on high-level use cases and target objectives determined during the PoC. This is still only an experimental stage. You may not want to be locked into any long-term commitments to one software vendor. Where possible, consider using subscription pricing and a hosted solution at least until the pilot has proven to be successful.</p>
    <p>Once in production, consider conducting regular experiments on a staging server that remains isolated from your production systems. These experiments should examine new product features, validate new releases, and verify patches and fixes. Use experiments to test new authoring techniques and publishing solutions before going live with them to production.</p>
    <h2>Governance strategies</h2>
    <p>Good governance is the key to scalability and sustainability of your program. When moving to a sophisticated, collaborative authoring solution, you need everyone playing by a common set of rules and guidelines. You need a strategy that addresses the needs of the business while catering to the needs of the team members responsible for carrying out the work. Governance needs to fit into the overall corporate strategy for managing its information assets. If executed well, you should see benefits such as a</p>
    <ul>
      <li>stable technology stack for authoring and publishing</li>
      <li>stable funding for skills development</li>
      <li>better opportunities for leveraging content from other departments</li>
      <li>better opportunities for others to reuse your content, and</li>
      <li>better opportunities for improvement and innovation.</li>
    </ul>
    <p>In 2015, Lantern Quill commissioned a study with IMA Guild entitled Rethinking Content Authoring and Reuse. This study polled more than 300 organizations from around the world about their content creation practices and technology. When respondents were asked about content standards in place to manage content creation, 16% indicated there are strict standards in place, while 47% acknowledged there is something there, but not strictly followed. For 37% the indication was that there is little to no use of standards in any form.</p>
    <p>Information Governance is the rocket fuel that empowers effective collaboration within and across teams and departments. Its purpose is to give everyone a voice in the future of the program and manage change across the enterprise. Good governance can be an important differentiator for your company.</p>
  </div>
</section>

<section class="page p7">
  <div class="masthead">
    <svg viewBox="0 0 300 64" preserveAspectRatio="none">
      <defs><linearGradient id="stripe7" x1="0" x2="1"><stop offset="0" stop-color="#3c8fd0"/><stop offset=".45" stop-color="#4aa9c0"/><stop offset="1" stop-color="#5fc0a8"/></linearGradient></defs>
      <rect width="300" height="24" fill="#1f55b4"/>
      <polygon points="0,24 300,24 300,50 238,50 226,62 0,62" fill="url(#stripe7)"/>
      <polygon points="0,46 300,38 300,46 0,52" fill="#2e6fc3" opacity=".55"/>
      <line x1="0" y1="62" x2="226" y2="62" stroke="#7fd0b0" stroke-width="1"/>
    </svg>
    <div class="brand"><span class="dot"></span>LANTERN QUILL</div>
    <div class="section-label">Management</div>
  </div>
  <div class="column" style="left:90px;top:82px;width:180px">
    <h2>Lantern Quill®<br>Information Governance Workshop</h2>
    <p>Let Lantern Quill help you build your governance strategy to engage both upper management and your team in a comprehensive, coordinated plan for moving forward with your structured authoring program. We'll help you to assess your maturity on the governance spectrum and lay out a path to a sustainable program. Working with our partners at IMA Guild, we will bring in industry-leading training and certification for your company to ensure success.</p>
    <h2>Conclusion</h2>
    <p>Don't let dissatisfaction derail your DITA project. Your greatest advancements in information management still to be achieved may not lie in the technology you use to manage content but in the content itself. Hundreds of companies have been working with structured authoring practices for producing intelligent content for more than a decade and found ways to reduce many of barriers to adoption including cost and complexity. You need not look too far to find practical advice and leverage lessons learned to bring their success into your organization. While this journey may seem daunting, it is one that should be taken seriously with a focus to begin with one element, and grow it out from there. The experts at Lantern Quill Authoring Solutions Inc. are pleased to support your journey and to share their knowledge. Call us today to help <b><i>Open the Knowledge in Your Enterprise™</i></b>.</p>
  </div>
  <div class="endnotes" style="left:40px;top:290px;width:226px">
    <p>[i] The Structured Content Contentment Poll, published by The Copy Ranch in spring 2017. An analysis of the results is in the TalkStage archive.</p>
    <p>[ii] Getting Ready to Manage Content, a talk by Reid Halvorsen at the Writers' Spring Gathering, 2009.</p>
    <p>[iii] Lessons From a Large Topic Library, a talk given at an online meetup of The Copy Ranch, 2016.</p>
    <p>[iv] Why Governance Opens Doors, a talk by Reid Halvorsen at the Content Builders Meetup, 2017.</p>
    <p>[v] Rethinking Content Authoring and Reuse, backed by Lantern Quill and published by IMA Guild in 2016, at lanternquill.com.</p>
  </div>
</section>

<section class="page p8">
  <div class="back-band"></div>
  <div class="back-col">
    <h3>ABOUT THE AUTHOR</h3>
    <p>Reid Halvorsen co-founded Lantern Quill in 2013 to change the way writers approach structured authoring. Having spent more than decade helping organizations move to component content management he realized that, to be successful, organizations need to take a step beyond technology and expert consultants. Without fostering the necessary standards and skills to work in this new media, organizations would continue to stall in their attempt to move to structured authoring. With this knowledge, he developed the Lantern Quill® methods, tools, and training. Today, Reid and his team of experts help Lantern Quill clients make the move to structured authoring.</p>
    <div class="spacer"></div>
    <h3>ABOUT LANTERN QUILL<br>AUTHORING SOLUTIONS INC.</h3>
    <p>Lantern Quill is a full-service solution provider to medium- and large-scale organizations around the globe seeking help to better understand and solve their content challenges. Our core services involve designing and implementing innovative, scalable, and sustainable solutions for authoring, managing, and publishing high-value content.</p>
  </div>
  <div class="back-brand"><span class="dot"></span>LANTERN QUILL</div>
</section>

</body>
</html>
```